Brennick Holdings Business Cards

These are professional business cards that are for my family office.
Put fake emails and phone numbers as of now until I finalize those components. This family office controls my families investments, assets, and future. The cards should be professional.
..
.
.
.
I just uploaded another variation of a logo I would like to see as a business card to I am inbeteen which logo to use

Target Market(s)

business

Industry/Entity Type

business

Contact Information for Business Card

Professional, wealth related, finance related.

Requirements
Must have
• Logo

```html
<!DOCTYPE html>
<html lang="en">
<head>
<meta charset="utf-8">
<title>Brennick Holdings Business Cards</title>
<link rel="stylesheet" href="https://fonts.googleapis.com/css2?family=Cinzel:wght@400&family=Lato:wght@400;700&display=swap">
<style>
  :root {
    --stage: #3b3c3f;
    --ink: #30333c;
    --paper: #ffffff;
    --muted: #a9a9a9;
    --text: #2a2c33;
  }
  * { box-sizing: border-box; margin: 0; padding: 0; }
  html, body { width: 1200px; height: 694px; overflow: hidden; }
  body {
    background: var(--stage);
    position: relative;
    font-family: "Lato", sans-serif;
  }
  .card {
    position: absolute;
    top: 192px;
    width: 540px;
    height: 310px;
    border-radius: 22px;
    box-shadow: 0 18px 40px rgba(0,0,0,0.35);
    overflow: hidden;
  }
  .card--front { left: 40px; background: var(--ink); }
  .card--back { left: 620px; background: var(--paper); }

  .brand {
    position: absolute;
    display: flex;
    flex-direction: column;
    align-items: center;
  }
  .brand__mark {
    width: 92px;
    height: 92px;
    border-radius: 50%;
    border: 3px solid currentColor;
    margin-bottom: 20px;
  }
  .brand__name {
    font-family: "Cinzel", serif;
    font-weight: 400;
    font-size: 30px;
    letter-spacing: 1px;
    white-space: nowrap;
  }
  .card--front .brand {
    color: var(--paper);
    left: 0; right: 0; top: 70px;
  }
  .card--back .brand {
    color: var(--ink);
    right: 34px; top: 70px;
  }
  .card--back .brand__mark { width: 100px; height: 100px; }
  .card--back .brand__name { font-size: 26px; }

  .contact {
    position: absolute;
    left: 34px;
    top: 74px;
    color: var(--text);
  }
  .contact__name { font-weight: 700; font-size: 23px; line-height: 1.1; }
  .contact__role { font-size: 14px; margin-top: 4px; }
  .contact__address { font-size: 14px; line-height: 1.35; margin-top: 26px; }
  .contact__list { list-style: none; margin-top: 22px; font-size: 14px; }
  .contact__list li { display: flex; align-items: center; gap: 10px; line-height: 1.55; }
  .contact__list svg { width: 13px; height: 13px; fill: var(--text); flex: none; }
</style>
</head>
<body>
  <section class="card card--front" aria-label="Card front">
    <div class="brand">
      <span class="brand__mark"></span>
      <span class="brand__name">Brennick Holdings</span>
    </div>
  </section>

  <section class="card card--back" aria-label="Card back">
    <div class="contact">
      <p class="contact__name">Daniel Hartley</p>
      <p class="contact__role">Owner</p>
      <p class="contact__address">421, Address line goes here<br>45452, Country name</p>
      <ul class="contact__list">
        <li>
          <svg viewBox="0 0 24 24" aria-hidden="true"><path d="M6.6 10.8a15.1 15.1 0 0 0 6.6 6.6l2.2-2.2c.3-.3.7-.4 1-.2 1.1.4 2.3.6 3.6.6.6 0 1 .4 1 1V20c0 .6-.4 1-1 1A17 17 0 0 1 3 4c0-.6.4-1 1-1h3.5c.6 0 1 .4 1 1 0 1.3.2 2.5.6 3.6.1.3 0 .7-.2 1z"/></svg>
          044-555 010 234
        </li>
        <li>
          <svg viewBox="0 0 24 24" aria-hidden="true"><path d="M2 5h20v14H2z M2 5l10 8 10-8" fill="none" stroke="#2a2c33" stroke-width="2"/></svg>
          info@brennickmail.com
        </li>
        <li>
          <svg viewBox="0 0 24 24" aria-hidden="true"><circle cx="12" cy="12" r="10"/></svg>
          www.brennicksite.com
        </li>
      </ul>
    </div>
    <div class="brand">
      <span class="brand__mark"></span>
      <span class="brand__name">Brennick Holdings</span>
    </div>
  </section>
</body>
</html>
```